Report presentation for measurement or inline reports

First page of report. Our inline reporting will come in a maintenance map. We want a modern first page and a real eye-catcher for a new company based in the Netherlands called: PRN Luchtcomfort B.V. We are a service company witch measures, balances and give advices at indoor climate HVAC installations. We would like to see designs that use the color blue. We deliver our services to different buildings: Hospitals, atractions, officebuildings, government buildings, swimming pools and schools. Our website: www.prnlc.nl
Updates

Can you all add the new logo please. The companyname is PRN Luchtcomfort B.V.. In witch format can i retrieve the design?

Industry/Entity Type

It Company

Colors
0255a3
3176b5
85abd2
cedeed
eaf1f7
ffffff

Requirements
Must have
• Projectname; projectplace; Inline or measure report; date; logo; companyname. it must be easy printable so not to much colours.
• The companyname is: PRN Luchtcomfort B.V.. Please add the name. A new logo is updated.
Nice to have
• Maybe some pictures from hvac installations, buildings or measure

```html
<!DOCTYPE html>
<html lang="en">
<head>
<meta charset="utf-8">
<title>Inline Report – Cover</title>
<link href="https://fonts.googleapis.com/css2?family=Roboto:wght@300;400;500&display=swap" rel="stylesheet">
<style>
  :root {
    --blue-dark: #0255a3;
    --blue: #3176b5;
    --blue-mid: #85abd2;
    --blue-light: #cedeed;
    --blue-pale: #eaf1f7;
    --white: #ffffff;
    --backdrop: #d9d9da;
    --text-dark: #2b2b2b;
    --text-soft: #6a6a6a;
  }
  html, body {
    margin: 0;
    width: 1200px;
    height: 1200px;
    overflow: hidden;
    background: var(--backdrop);
    font-family: "Roboto", Arial, sans-serif;
  }
  .cover {
    position: absolute;
    left: 220px;
    top: 40px;
    width: 760px;
    height: 1120px;
    background: linear-gradient(180deg, #f4f5f7 0%, #ffffff 45%, #eef0f2 100%);
    box-shadow: 0 6px 24px rgba(0,0,0,0.18);
    overflow: hidden;
  }
  .top-rule {
    position: absolute;
    left: 300px;
    right: 0;
    top: 158px;
    height: 8px;
    background: var(--blue);
  }
  .report-tab {
    position: absolute;
    left: 0;
    top: 130px;
    width: 340px;
    height: 64px;
    background: var(--blue);
    clip-path: polygon(0 0, 100% 0, 88% 100%, 0 100%);
    color: var(--white);
    font-size: 30px;
    font-weight: 400;
    line-height: 64px;
    padding-left: 44px;
    box-sizing: border-box;
    z-index: 2;
  }
  .photo-strip {
    position: absolute;
    left: 0;
    right: 0;
    top: 194px;
    height: 300px;
    display: flex;
  }
  .photo {
    flex: 1;
    border-left: 4px solid var(--white);
  }
  .photo:first-child { border-left: none; }
  .photo.condensers { background: linear-gradient(160deg, #b9bcc0, #7d8185 60%, #a6a9ad); }
  .photo.meter { background: linear-gradient(180deg, #eceeef, #c9ccce 60%, #b3b5b7); }
  .photo.ducts { background: linear-gradient(170deg, #c7ced6, #8e9aa6 55%, #b7c3d0); }
  .bottom-rule {
    position: absolute;
    left: 0;
    right: 0;
    top: 494px;
    height: 12px;
    background: var(--blue);
  }
  .title-block {
    position: absolute;
    left: 60px;
    top: 560px;
    z-index: 2;
  }
  .project-title {
    margin: 0;
    font-size: 44px;
    font-weight: 500;
    color: var(--text-dark);
  }
  .project-meta {
    margin: 14px 0 0;
    font-size: 32px;
    font-weight: 300;
    color: var(--text-soft);
    line-height: 1.3;
  }
  .swoosh {
    position: absolute;
    left: 0;
    top: 640px;
    width: 760px;
    height: 420px;
  }
  .brand {
    position: absolute;
    left: 250px;
    top: 965px;
    display: flex;
    align-items: center;
    gap: 14px;
    z-index: 2;
  }
  .brand-mark {
    width: 36px;
    height: 36px;
    background: var(--blue-dark);
  }
  .brand-name {
    font-size: 40px;
    font-weight: 500;
    color: var(--blue-dark);
  }
  .web-tab {
    position: absolute;
    left: 360px;
    top: 1040px;
    width: 330px;
    height: 90px;
    background: var(--blue);
    border-radius: 18px 18px 0 0;
    color: var(--white);
    font-size: 26px;
    text-align: center;
    line-height: 80px;
  }
</style>
</head>
<body>
  <main class="cover">
    <div class="top-rule"></div>
    <div class="report-tab">Inline Reporting</div>

    <div class="photo-strip">
      <div class="photo condensers" role="img" aria-label="Photo of rooftop HVAC condenser units with fans and piping"></div>
      <div class="photo meter" role="img" aria-label="Photo of a handheld measuring instrument held in front of ductwork"></div>
      <div class="photo ducts" role="img" aria-label="Photo of galvanised ventilation ducts under a warehouse ceiling"></div>
    </div>
    <div class="bottom-rule"></div>

    <div class="title-block">
      <h1 class="project-title">Testproject in Testplace</h1>
      <p class="project-meta">Measured by PRN Luchtcomfort B.V.<br>on 1-5-2017</p>
    </div>

    <svg class="swoosh" viewBox="0 0 760 420" aria-hidden="true">
      <path d="M470 90 L760 90 L760 130 C620 160 520 165 470 170 Z" fill="var(--blue)" opacity="0.85"/>
      <path d="M760 120 C560 210 260 250 0 255 L0 285 C280 280 580 240 760 165 Z" fill="var(--blue-dark)"/>
      <path d="M0 300 C260 295 560 260 760 190 L760 202 C560 272 260 310 0 315 Z" fill="var(--blue-mid)"/>
    </svg>

    <div class="brand">
      <span class="brand-mark"></span>
      <span class="brand-name">PRN Luchtcomfort</span>
    </div>

    <div class="web-tab">www.prnlc.nl</div>
  </main>
</body>
</html>
```